AV GLOSSUM BUSINESS CARD DESIGN PROJECT

We need to utilize our logo that was expertly created on Sketchloom and now need to match this with a business card design.

```html
<!DOCTYPE html>
<html lang="en">
<head>
<meta charset="utf-8">
<title>AV Glossum — Business Card</title>
<link href="https://fonts.googleapis.com/css2?family=Montserrat:wght@400;500;600;700&display=swap" rel="stylesheet">
<style>
  :root {
    --backdrop: #3a3a3a;
    --card-white: #ffffff;
    --card-dark: #2b2b2b;
    --brand-blue: #0a56b8;
    --brand-blue-light: #3d8ef0;
    --ink: #1c1c1c;
    --rule: #bdbdbd;
  }
  * { box-sizing: border-box; margin: 0; padding: 0; }
  html, body {
    width: 1200px; height: 1200px; overflow: hidden;
    background: var(--backdrop);
    font-family: "Montserrat", sans-serif;
  }
  .stage {
    width: 1200px; height: 1200px;
    display: flex; flex-direction: column;
    align-items: center; justify-content: center; gap: 60px;
  }
  .card {
    width: 700px; height: 400px;
    border-radius: 34px;
    position: relative;
    border-bottom: 5px solid var(--brand-blue);
    box-shadow: 0 14px 30px rgba(0,0,0,.35);
  }
  .card--front { background: var(--card-white); }
  .card--back {
    background: var(--card-dark);
    display: flex; align-items: center; justify-content: center;
  }
  .brand-name {
    font-weight: 700;
    color: var(--brand-blue);
    letter-spacing: 10px;
    white-space: nowrap;
  }
  .card--front .brand-name {
    position: absolute; top: 78px; left: 0; right: 0;
    text-align: center; font-size: 46px;
  }
  .card--back .brand-name { font-size: 52px; color: var(--brand-blue-light); }
  .holder {
    position: absolute; left: 60px; bottom: 70px;
  }
  .holder__name {
    font-size: 40px; font-weight: 700; color: var(--brand-blue);
    letter-spacing: -1.5px; line-height: 1;
  }
  .holder__position {
    font-size: 22px; font-weight: 500; color: var(--ink);
    letter-spacing: 1px; margin-top: 4px;
  }
  .divider {
    position: absolute; left: 380px; top: 215px;
    width: 1px; height: 125px; background: var(--rule);
  }
  .contact {
    position: absolute; left: 405px; top: 212px;
    list-style: none;
    font-size: 17px; color: var(--ink); line-height: 1.45;
  }
  .contact li { display: flex; align-items: flex-start; gap: 10px; }
  .contact svg { width: 18px; height: 18px; margin-top: 4px; flex: none; fill: var(--brand-blue); }
</style>
</head>
<body>
<main class="stage">
  <section class="card card--front">
    <div class="brand-name">AV GLOSSUM</div>
    <div class="holder">
      <div class="holder__name">FULL NAME</div>
      <div class="holder__position">POSITION</div>
    </div>
    <div class="divider"></div>
    <ul class="contact">
      <li>
        <svg viewBox="0 0 24 24"><path d="M6.6 10.8a15 15 0 0 0 6.6 6.6l2.2-2.2c.3-.3.7-.4 1-.2 1.1.4 2.3.6 3.6.6.6 0 1 .4 1 1V20c0 .6-.4 1-1 1A17 17 0 0 1 3 4c0-.6.4-1 1-1h3.5c.6 0 1 .4 1 1 0 1.3.2 2.5.6 3.6.1.3 0 .7-.2 1z"/></svg>
        <span>(000) 000 0000</span>
      </li>
      <li>
        <svg viewBox="0 0 24 24"><path d="M2 5h20v14H2z M2 5l10 8 10-8" fill="none" stroke="currentColor"/><path d="M2 5h20L12 13z"/><path d="M2 7l10 8 10-8v12H2z"/></svg>
        <span>email@company.com</span>
      </li>
      <li>
        <svg viewBox="0 0 24 24"><circle cx="12" cy="12" r="9" fill="none" stroke="#0a56b8" stroke-width="2"/><path d="M3 12h18M12 3c3 3 3 15 0 18M12 3c-3 3-3 15 0 18" fill="none" stroke="#0a56b8" stroke-width="1.5"/></svg>
        <span>www.company.com</span>
      </li>
      <li>
        <svg viewBox="0 0 24 24"><path d="M12 2a7 7 0 0 0-7 7c0 5 7 13 7 13s7-8 7-13a7 7 0 0 0-7-7zm0 9.5A2.5 2.5 0 1 1 12 6.5a2.5 2.5 0 0 1 0 5z"/></svg>
        <span>123 Name Street, 000<br>Your City, 00000-000</span>
      </li>
    </ul>
  </section>

  <section class="card card--back">
    <div class="brand-name">AV GLOSSUM</div>
  </section>
</main>
</body>
</html>
```